Crintle Homes from US$9,995– Making buying a house as easy as ordering a pizza online - worldwide

I am after a website that is fun and interactive.

Buying a house should be as simple as buying a Pizza delivery online.....

Margherita 20' ………………………………………….US$9,995
Standard, 30sqm Studio with kitchen & Bathroom, Flat Roof
Four Cheese 20' ………………………………………….US$11,995
Standard, 30sqm Studio with kitchen & Bathroom, Pitched Roof
Supreme 40' ………………………………………….US$18,995
Standard, 60sqm, 2 Bedrooms, Lounge, kitchen & Bathroom, Flat Roof
Pepperoni 40' ………………………………………….US$20,995
Standard, 60sqm, 2 Bedrooms, Lounge, kitchen & Bathroom, Pitched Roof
Hawaiian 40' ………………………………………….US$22,995
Beach design, 60sqm, 2 Bedrooms, Lounge, kitchen & Bathroom, Pitched Roof
The Works 40' ………………………………………….US$24,995
Beach design, 60sqm, 2 Bedrooms, Lounge, kitchen, Bathroom, Deck, Pitched Roof

eg. https://www.dishorbit.com.au/ https://www.crustvane.com

I want a fun design....

i want to reinvent how people DESIGN - BUILD and DELIVER housing

I want a SaaS solution for drop shipping pre-built houses.

The main campaign, we are offering 1,000 homes (to anywhere in the world) for US$9,995 + shipping

Just need to Pay a Fully refundable $100 Deposit to pre-register (so need a shopping cart & payment solution).

"Queue Jumper" - pay in full and jump the queue to get your Crintle months earlier.

The campaign is based on crowdsourcing - we need 1000 participants to pre-register - then everyone's orders will be filled .

The design is very simple...
HEADER
- The Story
- The Product
- Design our Own
- Pre-Register
- Contact Us

- Login
- Shopping Cart

FOOTER
- Privacy
- Terms & Conditions
- Investment
- Media
- NGO/Government
- Contact
- Sitemap

The important parts is that everyone who
- Subscribes
- Makes Contact
- Pre-registers
…in the system automatically gets an account (just need name and email address).
The user is then sent an email with details on how they can log back in at any time and see purchases, update profile (eg. Shipping address, contact details, etc....)

This data also needs to be sent to a CRM eg Leadmoor for marketing to automate regular updates to all users.

It also needs to link to Facebook, LinkedIn , TikTok, Instagram, Twitter

You can get sample content from our old website https://tenvaledwellings.webplotter.com/ - Plus I have attached updated content in this Brief.

The hero image should be a slider with videos and images with links to "Call to Action"

PLEASE NOTE: that "crintle" is a brand new product that we pre build offsite so when it is delivered, it is ready to move in to. So we need a whole new look and a new style

This is a wordpress site to be hosted on my server - Once completed I need full access to add, amend and update any pages, images products

I am very open to different colours - do not be limited by the colours in the logo.

I would be interested to see what you can do with NO white backgrounds. (This might look good or could look horrible)

And most importantly what will your design look like on mobile devices (phones / ipads)

SUCCESS (1) is getting the user to LOOK - DREAM - BUY (Or at least pre-register)

SUCCESS (2) it MUST look fun but still highly professional and TRUSTWORTHY to get the interest of investors to invest millions $$$$$

SUCCESS (3) we need to get "Inflencers / Bloggers" talking about Crintle - this could be done by a campaign to get a million likes and get a FREE home fo both the follower and the blogger

Target Market(s)

New home buyers (younger demographic), Families wanting to extend (middle aged)

Industry/Entity Type

Housing, Crowdsourcing, Drop shipping, SaaS technology

Coding

Coded - Design and coding required

Colors
0054AA
0677BA
7BADD7
CADEEF
E8F1F8
EE7325
F08F49
F5BC92
FAE3D3
FDF4ED

Requirements
Must have
• ecommerce, user accounts, social media & crm connections for crowdsourcing marketing, Call to actions
Nice to have
• $1,000,000
Should not have
• Do NOT complicate the funnel in the steps to sign-up

```html
<!DOCTYPE html>
<html lang="en">
<head>
<meta charset="utf-8">
<title>Crintle Homes</title>
<link href="https://fonts.googleapis.com/css2?family=Outfit:wght@300;400;500;600;700&display=swap" rel="stylesheet">
<style>
:root{
  --blue:#0054AA;--blue-2:#0677BA;--blue-3:#7BADD7;--blue-4:#CADEEF;--blue-5:#E8F1F8;
  --orange:#EE7325;--orange-2:#F08F49;--ink:#3b3f45;--muted:#6a6e75;--white:#fff;
}
*{box-sizing:border-box;margin:0;padding:0}
html,body{width:1200px;height:2967px;overflow:hidden}
body{font-family:"Outfit",sans-serif;color:var(--ink);background:var(--blue-5);position:relative}
a{text-decoration:none;color:inherit}
.btn{position:absolute;display:flex;align-items:center;justify-content:center;border-radius:16px;color:var(--white);font-size:10px;font-weight:600;text-transform:uppercase;letter-spacing:.3px}
.btn-orange{background:var(--orange)}
.btn-blue{background:var(--blue)}
.wordmark{font-weight:700;color:var(--blue);letter-spacing:1px;line-height:1}

/* header */
.site-header{position:absolute;left:0;top:0;width:1200px;height:94px;background:var(--white)}
.site-header .wordmark{position:absolute;left:106px;top:28px;font-size:44px}
.call{position:absolute;left:777px;top:23px;font-size:14px;color:var(--blue);display:flex;align-items:center;gap:6px}
.call b{color:var(--ink);font-weight:500}
.account{position:absolute;left:943px;top:15px;width:31px;height:31px;border-radius:50%;background:var(--blue);display:flex;align-items:center;justify-content:center}
.cart{left:987px;top:15px;width:106px;height:31px;font-size:9px;gap:5px}
.main-nav{position:absolute;top:66px;left:545px;display:flex;gap:36px;font-size:9.5px;text-transform:uppercase;color:var(--muted);font-weight:500}
.main-nav .active{color:var(--blue)}

/* hero */
.hero{position:absolute;left:0;top:94px;width:1200px;height:474px;overflow:hidden}
.hero-photo{position:absolute;inset:0;background:linear-gradient(180deg,#4a5a66 0%,#2c3238 45%,#23292b 65%,#3c4a2e 100%)}
.hero h1{position:absolute;top:120px;width:100%;text-align:center;color:var(--white);font-weight:300;font-size:38px;letter-spacing:.2px}
.hero h1 strong{font-weight:700}
.hero p{position:absolute;top:164px;width:100%;text-align:center;color:var(--white);font-size:30px;font-weight:300}
.hero .btn{left:547px;top:223px;width:106px;height:31px}
.roof-area{position:absolute;left:276px;width:646px;background:linear-gradient(180deg,rgba(0,84,170,.0) 0%,rgba(0,84,170,.35) 45%,var(--blue-5) 100%)}
.hero .roof-area{top:334px;height:140px}
.hero .roof-mark{position:absolute;left:0;top:434px;width:100%;text-align:center;font-size:34px}

/* welcome */
.welcome{position:absolute;left:0;top:568px;width:1200px;height:282px;background:var(--blue-5);text-align:center}
.section-title{font-size:31px;font-weight:300;color:var(--ink);text-transform:uppercase}
.section-title strong{font-weight:700;color:var(--blue)}
.welcome .section-title{margin-top:55px}
.welcome p{width:745px;margin:16px auto 0;font-size:15px;line-height:18.5px;color:var(--muted);font-weight:300}
.welcome .btn{left:547px;top:187px;width:106px;height:30px}

/* products */
.products{position:absolute;left:0;top:850px;width:1200px;height:739px;background:linear-gradient(180deg,#fafbfc,#efefef);text-align:center;box-shadow:inset 0 6px 8px -6px rgba(0,0,0,.12)}
.products .section-title{margin-top:55px}
.products .lead{margin-top:14px;font-size:15px;color:var(--ink)}
.products .intro{width:805px;margin:2px auto 0;font-size:15px;line-height:18.5px;color:var(--muted);font-weight:300}
.products .intro + .intro{margin-top:18px}
.features{position:absolute;left:200px;top:280px;width:390px;text-align:left}
.feature{height:75px}
.feature h3{font-size:14px;font-weight:500;color:var(--blue)}
.feature p{margin-top:14px;font-size:10.5px;line-height:15px;color:var(--muted);font-weight:300}
.products .btn{left:200px;top:596px;width:119px;height:30px}
.product-photo{position:absolute;left:613px;top:239px;width:387px;height:438px;background:linear-gradient(180deg,#7aa3d4 0%,#b9cfe6 35%,#d9dcdc 60%,#8a8f88 80%,#6f7a56 100%)}

/* pricing */
.design{position:absolute;left:0;top:1589px;width:1200px;height:528px;background:var(--white);text-align:center}
.design .section-title{margin-top:57px}
.plan{position:absolute;top:111px;width:312px;height:354px;background:var(--blue-5);border:2px solid var(--blue);border-bottom-right-radius:50px;overflow:hidden}
.plan-standard{left:275px}
.plan-upsize{left:613px;border-color:var(--orange)}
.plan-banner{position:absolute;left:-2px;top:-2px}
.plan-name{position:absolute;top:29px;width:100%;font-size:11px;color:var(--white);text-transform:uppercase}
.plan-price{position:absolute;top:78px;width:100%;font-size:22px;color:var(--blue)}
.plan-upsize .plan-price{color:var(--orange)}
.plan-list{position:absolute;left:0;top:113px;width:100%;list-style:none;text-align:left}
.plan-list li{border-top:1px dashed #b9c7d6;padding:14px 52px 14px 73px;font-size:11.5px;line-height:19px;position:relative;color:var(--ink)}
.plan-list li:last-child{border-bottom:1px dashed #b9c7d6}
.plan-list svg{position:absolute;left:48px;top:20px}
.plan .btn{left:76px;top:316px;width:156px;height:36px;border-radius:0;font-size:9px}

/* pre-register */
.preregister{position:absolute;left:0;top:2117px;width:1200px;height:549px;background:#6c6f74;text-align:center;color:var(--white)}
.preregister .section-title{margin-top:58px;color:var(--white)}
.preregister .section-title strong{color:var(--white)}
.step{position:absolute;top:121px;width:240px;text-align:center}
.step-icon{width:88px;height:88px;margin:0 auto;border-radius:50%;background:var(--white);border:2px solid var(--orange);position:relative;display:flex;align-items:center;justify-content:center}
.step-num{position:absolute;bottom:-8px;left:35px;width:17px;height:17px;border-radius:50%;background:var(--orange);font-size:8px;line-height:17px;color:var(--white)}
.step h3{margin-top:18px;font-size:14.5px;font-weight:500}
.step p{margin-top:12px;font-size:11px;line-height:15.5px;font-weight:300}
.preregister .btn{left:541px;top:315px;width:118px;height:30px}
.preregister .roof-area{top:409px;height:140px}

/* footer */
.site-footer{position:absolute;left:0;top:2666px;width:1200px;height:301px;background:var(--blue-5)}
.site-footer .wordmark{position:absolute;left:200px;top:70px;font-size:36px}
.socials{position:absolute;left:212px;top:130px;display:flex;gap:8px}
.socials span{width:24px;height:24px;border-radius:50%;background:#4d5359}
.socials span.on{background:var(--orange)}
.footer-col{position:absolute;top:62px}
.footer-col h4{font-size:15px;font-weight:500;color:var(--ink)}
.contact{left:406px}
.contact li{list-style:none;position:relative;padding-left:22px;font-size:9px;margin-top:10px;color:var(--ink)}
.contact li.phone{font-size:15px;margin-top:14px}
.contact li svg{position:absolute;left:0;top:1px}
.contact .brand{color:var(--orange)}
.links{left:613px}
.links li{list-style:none;font-size:9px;line-height:19px;color:var(--ink)}
.links ul{margin-top:12px}
.newsletter{left:762px}
.newsletter input{display:block;margin-top:15px;width:250px;height:35px;border:1px solid var(--blue-3);border-radius:18px;padding:0 18px;font-family:inherit;font-size:9px;background:var(--white);color:var(--ink)}
.newsletter .btn{position:relative;margin-top:15px;width:88px;height:29px;font-size:8.5px}
.copyright{position:absolute;left:200px;top:242px;font-size:9px;color:var(--ink)}
.copyright span{color:var(--blue)}
.to-top{position:absolute;left:1093px;top:232px}
</style>
</head>
<body>

<header class="site-header">
  <a class="wordmark" href="#">CRINTLE</a>
  <div class="call">Call Us:
    <svg width="12" height="12" viewBox="0 0 24 24"><path fill="#0054AA" d="M6.6 10.8a15 15 0 0 0 6.6 6.6l2.2-2.2a1 1 0 0 1 1-.25 11.4 11.4 0 0 0 3.6.57 1 1 0 0 1 1 1V20a1 1 0 0 1-1 1A17 17 0 0 1 3 4a1 1 0 0 1 1-1h3.5a1 1 0 0 1 1 1c0 1.25.2 2.45.57 3.57a1 1 0 0 1-.25 1z"/></svg>
    <b>041 555 0193</b></div>
  <a class="account" href="#" aria-label="Login"><svg width="10" height="10" viewBox="0 0 24 24"><circle cx="12" cy="8" r="5" fill="#fff"/><path d="M3 22c0-5 4-8 9-8s9 3 9 8z" fill="#fff"/></svg></a>
  <a class="btn btn-orange cart" href="#"><svg width="10" height="10" viewBox="0 0 24 24"><path fill="#fff" d="M2 3h3l3 11h11l3-8H7"/><circle cx="9" cy="19" r="2" fill="#fff"/><circle cx="18" cy="19" r="2" fill="#fff"/></svg>Cart $0.00</a>
  <nav class="main-nav">
    <a class="active" href="#">- Home -</a><a href="#">The Story</a><a href="#">Our Products</a><a href="#">Design Our Own</a><a href="#">Pre-Register</a><a href="#">Contact Us</a>
  </nav>
</header>

<section class="hero">
  <div class="hero-photo" role="img" aria-label="Dark clad modular home at dusk on a lawn among trees"></div>
  <h1>CRINTLE HOMES FROM <strong>US$9,995</strong></h1>
  <p>Making buying a house as easy as ordering a pizza online!</p>
  <a class="btn btn-orange" href="#">Contact Us</a>
  <div class="roof-area" role="img" aria-label="Blue house roof decoration framing the brand name"></div>
  <div class="wordmark roof-mark">CRINTLE</div>
</section>

<section class="welcome">
  <h2 class="section-title">Welcome to <strong>Crintle</strong></h2>
  <p>Building a house should not be stressful – we believe it should be the happiest and one of the most rewarding experiences in your lifetime. So we set up our Happiness Brains Trust to troubleshoot how to remove the stress, delays and unexpected costs from building.</p>
  <a class="btn btn-blue" href="#">Our Story</a>
</section>

<section class="products">
  <h2 class="section-title">Our <strong>Products</strong></h2>
  <p class="lead">What is a Crintle home</p>
  <p class="intro">It is simple through very clever engineering we build your full house in our factories including all electrical, plumbing, shelves, benches, lights, fans, window, doors….and even the kitchen sink. Once we have completed construction, we cleverly fold it up ready to ship.</p>
  <p class="intro">Once it arrive at your property, within hours you can have it unfolded and ready to move in to – it is that easy</p>
  <div class="features">
    <div class="feature"><h3>Every Design is Unique</h3><p>Use our easy online tools to design your own unique home with different colours, kitchens, bathrooms, flooring, etc ...</p></div>
    <div class="feature"><h3>Fast Construction</h3><p>Within 24 hours of designing your house, our busy elfs will start construction on your dream – In under 4 weeks we will ...</p></div>
    <div class="feature"><h3>Reliable Shipping</h3><p>Our shippers are fully insured and we shrink wrap for safe travel. Shipping can take 1 – 4 weeks (depending on your location) ...</p></div>
    <div class="feature"><h3>Minimal Permits</h3><p>Every local government can have different bi-laws, but as our core construction is pre-engineered in our factories ...</p></div>
  </div>
  <a class="btn btn-blue" href="#">Discover More</a>
  <div class="product-photo" role="img" aria-label="Two storey white modular house with dark balcony and paved driveway"></div>
</section>

<section class="design">
  <h2 class="section-title"><strong>Design</strong> Our Own</h2>
  <div class="plan plan-standard">
    <svg class="plan-banner" width="312" height="68" viewBox="0 0 312 68"><polygon points="0,0 312,0 156,68" fill="#0054AA"/></svg>
    <div class="plan-name">Standard</div>
    <div class="plan-price">US$9,995</div>
    <ul class="plan-list">
      <li><svg width="13" height="8" viewBox="0 0 13 8"><path d="M1 4l2.5 3L8 1M5 5.5L6.5 7 12 1" stroke="#0677BA" fill="none" stroke-width="1.2"/></svg>Each module is 6.0m x 5.0m<br>(30 sqm)</li>
      <li><svg width="13" height="8" viewBox="0 0 13 8"><path d="M1 4l2.5 3L8 1M5 5.5L6.5 7 12 1" stroke="#0677BA" fill="none" stroke-width="1.2"/></svg>The yellow section of each module<br>can be interchanged</li>
      <li><svg width="13" height="8" viewBox="0 0 13 8"><path d="M1 4l2.5 3L8 1M5 5.5L6.5 7 12 1" stroke="#0677BA" fill="none" stroke-width="1.2"/></svg>The white area is open plan and<br>you can add partition walls.</li>
    </ul>
    <a class="btn btn-blue" href="#">Get Started Today</a>
  </div>
  <div class="plan plan-upsize">
    <svg class="plan-banner" width="312" height="68" viewBox="0 0 312 68"><polygon points="0,0 312,0 156,68" fill="#EE7325"/></svg>
    <div class="plan-name">Upsize</div>
    <div class="plan-price">US$18,995</div>
    <ul class="plan-list">
      <li><svg width="13" height="8" viewBox="0 0 13 8"><path d="M1 4l2.5 3L8 1M5 5.5L6.5 7 12 1" stroke="#EE7325" fill="none" stroke-width="1.2"/></svg>Each module is 6.0m x 5.0m<br>(30 sqm)</li>
      <li><svg width="13" height="8" viewBox="0 0 13 8"><path d="M1 4l2.5 3L8 1M5 5.5L6.5 7 12 1" stroke="#EE7325" fill="none" stroke-width="1.2"/></svg>Or you can upsize to our larger<br>models that are 60sqm each eg.<br>Add 2 together and you have<br>120sqm</li>
    </ul>
    <a class="btn btn-orange" href="#">Get Started Today</a>
  </div>
</section>

<section class="preregister" role="img" aria-label="Modular home exterior behind a grey overlay">
  <h2 class="section-title"><strong>Pre</strong> Register</h2>
  <div class="step" style="left:205px">
    <div class="step-icon"><svg width="30" height="30" viewBox="0 0 24 24"><path d="M4 20l1-5L16 4l4 4L9 19z M14 6l4 4" stroke="#0054AA" fill="none" stroke-width="1.5" stroke-linejoin="round"/></svg><span class="step-num">1</span></div>
    <h3>Easy Pre-Registration</h3>
    <p>Lorem Ipsum is simply dummy text of the<br>and typesetting industry.</p>
  </div>
  <div class="step" style="left:480px">
    <div class="step-icon"><svg width="30" height="30" viewBox="0 0 24 24"><rect x="5" y="4" width="14" height="17" rx="1" stroke="#0054AA" fill="none" stroke-width="1.5"/><rect x="9" y="2.5" width="6" height="3" fill="#0054AA"/><path d="M8 10h8M8 13.5h8M8 17h8" stroke="#0054AA" stroke-width="1.5"/></svg><span class="step-num">1</span></div>
    <h3>Choose one of Option</h3>
    <p>Lorem Ipsum is simply dummy text of the<br>and typesetting industry.</p>
  </div>
  <div class="step" style="left:755px">
    <div class="step-icon"><svg width="30" height="30" viewBox="0 0 24 24"><path d="M3 10l9-6 9 6v10H3z M3 10l9 6 9-6" stroke="#0054AA" fill="none" stroke-width="1.5" stroke-linejoin="round"/></svg><span class="step-num">1</span></div>
    <h3>Confirmation Mail</h3>
    <p>Lorem Ipsum is simply dummy text of the<br>and typesetting industry.</p>
  </div>
  <a class="btn btn-orange" href="#">Pre Register</a>
  <div class="roof-area" role="img" aria-label="Blue house roof decoration leading into the footer"></div>
</section>

<footer class="site-footer">
  <div class="wordmark">CRINTLE</div>
  <div class="socials" aria-label="Social links"><span></span><span class="on"></span><span></span><span></span><span></span></div>
  <div class="footer-col contact">
    <h4>Contact Us</h4>
    <ul>
      <li class="phone"><svg width="12" height="12" viewBox="0 0 24 24"><path fill="#EE7325" d="M6.6 10.8a15 15 0 0 0 6.6 6.6l2.2-2.2a1 1 0 0 1 1-.25 11.4 11.4 0 0 0 3.6.57 1 1 0 0 1 1 1V20a1 1 0 0 1-1 1A17 17 0 0 1 3 4a1 1 0 0 1 1-1h3.5a1 1 0 0 1 1 1c0 1.25.2 2.45.57 3.57a1 1 0 0 1-.25 1z"/></svg>041 555 0193</li>
      <li><svg width="10" height="10" viewBox="0 0 24 24"><path fill="#EE7325" d="M2 5h20v14H2z"/><path d="M2 5l10 8 10-8" stroke="#fff" fill="none" stroke-width="2"/></svg>info@crintle.com</li>
      <li><svg width="10" height="11" viewBox="0 0 24 24"><path fill="#EE7325" d="M12 2a7 7 0 0 0-7 7c0 5 7 13 7 13s7-8 7-13a7 7 0 0 0-7-7zm0 9.5A2.5 2.5 0 1 1 12 6.5a2.5 2.5 0 0 1 0 5z"/></svg><span class="brand">CRINTLE</span><br>PO 742, Larkfield, Victoria 3988,<br>AUSTRALIA</li>
    </ul>
  </div>
  <div class="footer-col links">
    <h4>Quick Links</h4>
    <ul><li>Privacy</li><li>Terms &amp; Conditions</li><li>Investment</li><li>Media</li><li>NGO/Government</li><li>Contact</li><li>Sitemap</li></ul>
  </div>
  <div class="footer-col newsletter">
    <h4>Subscribe Newsletter</h4>
    <input type="email" placeholder="name@email.com" aria-label="Email address">
    <a class="btn btn-orange" href="#">Subscribe</a>
  </div>
  <p class="copyright">2023 <span>Crintle</span>. All Rights Reserved.</p>
  <svg class="to-top" width="24" height="30" viewBox="0 0 24 30" aria-label="Back to top"><polygon points="12,0 24,30 12,23 0,30" fill="#0054AA"/></svg>
</footer>

</body>
</html>
```